Be Still.....Business Card Design

I am a life coach with a holistic earthy spiritual approach to coaching. The colours I use are the turquoise green range with three large dots going from lighter to darker as a symbol of progression. The main purpose of the card is give my contact details and to write the appointment time and date on the back My tag line is "positive results with a personal touch" I've attached a template I made myself for my invoices the colour isn't as turquoise as I'd like. I don't like block letters I prefer a softer font but not script. I also like tan colours and beachy themes. After the name Be Still...... there are at least five dots before the Life Coaching.

Industry/Entity Type

Business

Contact Information for Business Card

Helen Marsh
42 Lorikeet Street
Seabrook 4812

```html
<!DOCTYPE html>
<html lang="en">
<head>
<meta charset="utf-8">
<title>Be Still – Business Card</title>
<link rel="stylesheet" href="https://fonts.googleapis.com/css2?family=Andika:wght@400;700&display=swap">
<style>
  :root {
    --page: #f2f2f2;
    --card: #fdfbef;
    --ink: #1c1c1c;
    --turquoise: #5fe0c0;
    --turquoise-pale: #c9f3e7;
    --label: #222;
  }
  * { box-sizing: border-box; margin: 0; padding: 0; }
  html, body {
    width: 1200px; height: 1200px; overflow: hidden;
    background: var(--page);
    font-family: "Andika", sans-serif;
    color: var(--ink);
  }
  .sheet { position: relative; width: 1200px; height: 1200px; }
  .card {
    position: absolute; top: 400px; width: 520px; height: 322px;
    background: var(--card);
    box-shadow: 6px 8px 14px rgba(0,0,0,0.28);
  }
  .card--front { left: 60px; }
  .card--back { left: 620px; }
  .side-label {
    position: absolute; top: 758px; width: 520px; text-align: center;
    font-size: 17px; letter-spacing: 0.5px; color: var(--label);
  }
  .side-label--front { left: 60px; }
  .side-label--back { left: 620px; }

  /* Front */
  .ornament {
    position: absolute; left: 228px; top: 28px; width: 150px; height: 150px;
    border-radius: 50%;
    background: radial-gradient(circle, var(--turquoise-pale) 0%, rgba(201,243,231,0.35) 60%, rgba(201,243,231,0) 75%);
  }
  .brand-name {
    position: absolute; left: 0; width: 520px; top: 92px; text-align: center;
    font-size: 60px; font-weight: 700; line-height: 1; color: var(--ink);
  }
  .brand-service {
    position: absolute; left: 296px; top: 170px;
    font-size: 16px; font-variant: small-caps; letter-spacing: 0.5px;
  }
  .tagline {
    position: absolute; left: 0; width: 520px; top: 204px; text-align: center;
    font-size: 12px; font-weight: 700; font-variant: small-caps; letter-spacing: 0.6px;
  }
  .contact {
    position: absolute; left: 56px; top: 268px; display: flex; align-items: baseline; gap: 10px;
  }
  .contact__name { font-size: 20px; color: var(--turquoise); font-variant: small-caps; }
  .contact__address { font-size: 12px; font-weight: 700; font-variant: small-caps; letter-spacing: 0.4px; }

  /* Back */
  .rule { position: absolute; height: 2px; background: var(--turquoise); }
  .rule--top { left: 50px; width: 420px; top: 90px; }
  .rule--date { left: 96px; width: 210px; top: 198px; }
  .rule--time { left: 330px; width: 70px; top: 198px; }
  .appt-heading {
    position: absolute; left: 0; width: 520px; top: 104px; text-align: center;
    font-size: 12px; font-weight: 700; font-variant: small-caps;
  }
  .days {
    position: absolute; left: 88px; top: 140px; display: flex; gap: 34px;
    font-size: 12px; font-weight: 700; font-variant: small-caps;
  }
  .day { display: flex; align-items: center; gap: 5px; }
  .day__box { width: 12px; height: 12px; border: 2px solid var(--turquoise); }
  .at { position: absolute; left: 312px; top: 188px; font-size: 10px; font-weight: 700; font-variant: small-caps; }
  .ampm { position: absolute; left: 404px; top: 170px; font-size: 12px; font-weight: 700; line-height: 1.2; }
  .notice {
    position: absolute; left: 0; width: 520px; top: 244px; text-align: center;
    font-size: 13px; font-weight: 700; font-variant: small-caps;
  }
  .progress-dots { position: absolute; left: 200px; top: 277px; display: flex; gap: 24px; }
  .progress-dots span { width: 5px; height: 5px; border-radius: 50%; background: var(--turquoise); }
</style>
</head>
<body>
<main class="sheet">
  <section class="card card--front" aria-label="Business card front">
    <div class="ornament" role="img" aria-label="Soft turquoise shell and flower line ornament"></div>
    <div class="brand-name">Be Still</div>
    <div class="brand-service">Life Coaching</div>
    <p class="tagline">~ Positive results with a personal touch ~</p>
    <div class="contact">
      <span class="contact__name">Helen Marsh</span>
      <span class="contact__address">42 Lorikeet Street Seabrook 4812</span>
    </div>
  </section>

  <section class="card card--back" aria-label="Business card back">
    <div class="rule rule--top"></div>
    <p class="appt-heading">has an appointment on</p>
    <div class="days">
      <span class="day"><span class="day__box"></span>Mon.</span>
      <span class="day"><span class="day__box"></span>Tues.</span>
      <span class="day"><span class="day__box"></span>Wed.</span>
      <span class="day"><span class="day__box"></span>Thurs.</span>
      <span class="day"><span class="day__box"></span>Fri.</span>
    </div>
    <div class="rule rule--date"></div>
    <span class="at">at</span>
    <div class="rule rule--time"></div>
    <div class="ampm">A.M.<br>P.M.</div>
    <p class="notice">If unable to keep appointment kindly give 24 hours notice.</p>
    <div class="progress-dots"><span></span><span></span><span></span><span></span><span></span></div>
  </section>

  <div class="side-label side-label--front">FRONT</div>
  <div class="side-label side-label--back">BACK</div>
</main>
</body>
</html>
```